Lueur de Provins Immerse in the enchanting flavors of France at Lueur de Provins

A menu that is French in style with the Eiffel Tower. A elegant menu that is in rich blue with red or gold trimmings, we are a French Bakey and Cafe

Target Market(s)

30 to 55 people

Industry/Entity Type

Restaurant

Font styles to use
Decorative

Colors
0054AA
0677BA
7BADD7
CADEEF
E8F1F8
EB3D1F
EC4F4E
F09395
F8D3D4
FCEDEE

Requirements
Must have
• the attachment "My Brunch Specials" is the Menu I want you to create, it has all the text, "My Brunch Special Complete" is a word version. The menu size should be 4 1/4 wide by 14 inches long 2 Sided. must have our logo at the top , Make the font larger, because our biggest complaint about our menu is it is hard to read
Nice to have
• I would love to incorporate the Eiffel Tower as a silhouette in the background
Should not have
• I do not want too many pictures or small print

```html
<!DOCTYPE html>
<html lang="en">
<head>
<meta charset="utf-8">
<title>Lueur de Provins – Brunch &amp; Drinks Menu</title>
<link rel="stylesheet" href="https://fonts.googleapis.com/css2?family=Great+Vibes&family=Roboto+Slab:wght@700&family=Archivo+Narrow:wght@400;500&display=swap">
<style>
  :root{
    --backdrop:#3f3f3f;
    --paper:#f7f6f4;
    --red:#c9403a;
    --navy:#1b2b52;
    --ink:#2a2a2a;
    --tower-red-top:rgba(201,64,58,.04);
    --tower-red-bottom:rgba(201,64,58,.22);
    --tower-navy-top:rgba(27,43,82,.04);
    --tower-navy-bottom:rgba(27,43,82,.22);
  }
  *{margin:0;padding:0;box-sizing:border-box}
  html,body{width:1200px;height:2536px;overflow:hidden;background:var(--backdrop)}
  .canvas{position:relative;width:1200px;height:2536px}
  .panel{
    position:absolute;top:329px;width:570px;height:1878px;
    background:var(--paper);overflow:hidden;
    box-shadow:0 2px 6px rgba(0,0,0,.35);
  }
  .panel--brunch{left:20px}
  .panel--drinks{left:610px}
  .frame-outer{position:absolute;inset:12px;border:2px solid var(--red)}
  .frame-inner{position:absolute;inset:18px;border:1px solid var(--navy)}

  .brand{
    position:absolute;left:0;right:0;top:148px;text-align:center;
    font-family:"Archivo Narrow",sans-serif;font-weight:500;
    font-size:24px;letter-spacing:.42em;color:var(--navy);
  }
  .section-title{
    position:absolute;left:0;right:0;text-align:center;
    font-family:"Great Vibes",cursive;font-weight:400;line-height:1;
  }
  .section-title--brunch{top:205px;font-size:80px;color:var(--red)}
  .section-title--drinks{top:44px;font-size:80px;color:var(--navy)}
  .section-title--latte{top:1150px;font-size:72px;color:var(--red)}

  .item{position:absolute;z-index:1}
  .item--center{left:40px;right:40px;text-align:center}
  .item--left{left:40px;text-align:left}
  .label{
    display:inline-block;height:38px;line-height:38px;padding:0 26px;
    font-family:"Roboto Slab",serif;font-weight:700;font-size:24px;color:#fff;
    white-space:nowrap;
    clip-path:polygon(0 0,100% 0,calc(100% - 7px) 50%,100% 100%,0 100%,7px 50%);
  }
  .label .price{margin-left:22px}
  .label--red{background:var(--red)}
  .label--navy{background:var(--navy)}
  .label--small{font-size:22px;padding:0 20px}
  .desc{
    margin-top:6px;font-family:"Archivo Narrow",sans-serif;font-size:16px;
    line-height:22.5px;color:var(--ink);
  }
  .desc--compact{font-size:15px;line-height:20.8px}

  .tower{position:absolute;z-index:0;border-radius:48px 48px 0 0}
  .tower--red{left:19px;top:1380px;width:96px;height:480px;
    background:linear-gradient(180deg,var(--tower-red-top),var(--tower-red-bottom))}
  .tower--navy{left:460px;top:1420px;width:91px;height:440px;
    background:linear-gradient(180deg,var(--tower-navy-top),var(--tower-navy-bottom))}
</style>
</head>
<body>
<main class="canvas">

  <section class="panel panel--brunch">
    <div class="frame-outer"></div>
    <div class="frame-inner"></div>

    <div class="brand">LUEUR DE PROVINS</div>
    <h1 class="section-title section-title--brunch">Brunch Special</h1>

    <div class="tower tower--red" role="img" aria-label="Red line illustration of the Eiffel Tower"></div>

    <article class="item item--center" style="top:331px">
      <span class="label label--red">Ratatouille &amp; Eggs<span class="price">$18</span></span>
      <p class="desc">Experience the essence of Provence with our Ratatouille, a vibrant medley of roasted squash, peppers, tomatoes, eggplant, infused with fragrant fresh herbs. Served with two perfectly poached eggs, and your choice of flavorful andouille sausage or crispy bacon. Accompanied by a side of crusty baguette. It's a hearty dish that celebrates the flavors of the Mediterranean countryside.</p>
    </article>

    <article class="item item--center" style="top:538px">
      <span class="label label--red">Le Grande Breakfast<span class="price">$15</span></span>
      <p class="desc">Start your day in style with our Le Grande Breakfast, a feast fit for royalty. Customize your morning indulgence with two eggs cooked to your preference, paired with either savory bacon or succulent chicken sausage. Choose between a freshly baked baguette or a buttery croissant to accompany your meal. Complete your breakfast by selecting from an array of sides including crispy hash browns, savory roasted potatoes, or a refreshing fruit salad. Bon appetit!</p>
    </article>

    <article class="item item--center" style="top:776px">
      <span class="label label--red">Smoked Salmon Tartine<span class="price">$14</span></span>
      <p class="desc">Delight in the luxurious flavors of our Smoked Salmon Tartine, a culinary masterpiece that elevates breakfast to new heights. Indulge in truffled scrambled eggs nestled atop smoked salmon, adorned with tangy pickled red onions, briny caper berries, crisp cucumber, juicy tomato, and peppery arugula. All artfully arranged on multigrain bread generously spread with herb-infused cream cheese.</p>
    </article>

    <article class="item item--center" style="top:1013px">
      <span class="label label--red">Le Benedict Salmon<span class="price">$14</span></span>
      <p class="desc">Savor the classic elegance of Eggs Benedict, featuring two perfectly poached eggs nestled on toasted English muffins, with luscious smoked salmon and ripe tomato slices crowned with a velvety lemon-infused Hollandaise sauce. A timeless brunch delight crafted to perfection.</p>
    </article>

    <article class="item item--center" style="top:1206px">
      <span class="label label--red">Salmon Atlantique<span class="price">$14</span></span>
      <p class="desc">Enjoy a bed of crisp mixed greens adorned with delicate smoked salmon, sweet golden raisins, creamy goat cheese, and crunchy walnuts. All dressed in a tantalizing balsamic vinaigrette that ties the elements together perfectly.</p>
    </article>

    <article class="item item--center" style="top:1382px;left:125px">
      <span class="label label--red">Beef Bourguignon<span class="price">$18</span></span>
      <p class="desc">Indulge in our rich and comforting flavors of savory, tender beef slowly braised in red wine, creating a luscious sauce that envelops pearl onions, carrots, and mushrooms in a symphony of flavors. Served alongside buttered egg noodles. It's a hearty and soul-warming meal that promises pure culinary bliss.</p>
    </article>

    <article class="item item--center" style="top:1616px;left:165px">
      <span class="label label--red">Tourte au Poulet<span class="price">$15</span></span>
      <p class="desc">Discover the indulgent flavors of our Tourte au Poulet, a savory delight that marries tender marinated chicken with the richness of Swiss cheese and the sweetness of onions, all encased in layers of flaky pastry. Topped with a savory mushroom medley and decadent bechamel sauce. A true comfort classic to delight your senses.</p>
    </article>
  </section>

  <section class="panel panel--drinks">
    <div class="frame-outer"></div>
    <div class="frame-inner"></div>

    <h2 class="section-title section-title--drinks">Drinks Special</h2>

    <div class="tower tower--navy" role="img" aria-label="Navy line illustration of the Eiffel Tower"></div>

    <article class="item item--center" style="top:151px">
      <span class="label label--navy">Bottomless Mimosa<span class="price">$18</span></span>
      <p class="desc">Embark on an endless journey of delight with our Bottomless Mimosa, featuring Ashcombe champagne, infusing each sip with a sparkling sensation. Tailor your experience with your preferred flavor profile - opt for the timeless twist of classic orange juice or tangy cranberry juice for a refreshing zing. Continuously poured to ensure your glass is always full.</p>
    </article>

    <article class="item item--center" style="top:356px">
      <span class="label label--navy">Apple Cider-Mimosa<span class="price">$9</span></span>
      <p class="desc">A delightful twist on the classic mimosa. Crafted with champagne and crisp apple cider. To elevate the experience, we adorn the glass with a caramel rim dipped in brown sugar, adding a touch of indulgent sweetness to every sip.</p>
    </article>

    <article class="item item--center" style="top:517px">
      <span class="label label--navy label--small">Blood Orange or Pineapple Spritz<span class="price">$12</span></span>
      <p class="desc">Introducing our vibrant spritz cocktail, a tantalizing blend of Marlowe &amp; Reed's premium Vesnaya Vodka, sweet vermouth, and a touch of sweetness from a carefully muddled sugar cube. This effervescent libation reaches new heights with the addition of bubbly Belcourt, your choice of either Blood Orange or Pineapple syrup injects a burst of fruity allure into every sip.</p>
    </article>

    <article class="item item--center" style="top:722px">
      <span class="label label--navy">Peach Bellini<span class="price">$9</span></span>
      <p class="desc">Try our perfectly balanced Peach Bellini with each sip you capture the crispness of champagne with the irresistible sweetness of peach. It's a sublime fusion of sophistication and sweetness.</p>
    </article>

    <article class="item item--center" style="top:859px">
      <span class="label label--navy">Espresso Martini<span class="price">$10</span></span>
      <p class="desc">Our Espresso Martini is a decadent blend of bold espresso, rich chocolate martini, and luxurious Caravelle chocolate syrup. It's the ultimate indulgence for coffee and chocolate lovers alike.</p>
    </article>

    <article class="item item--center" style="top:998px">
      <span class="label label--navy">Kir Royale<span class="price">$10</span></span>
      <p class="desc">Our Espresso Martini is a decadent blend of bold espresso, rich chocolate martini, and luxurious Caravelle chocolate syrup. It's the ultimate indulgence for coffee and chocolate lovers alike.</p>
    </article>

    <h3 class="section-title section-title--latte">Latte</h3>

    <article class="item item--left" style="top:1243px;right:35px">
      <span class="label label--red">Truffle Latte<span class="price">$6</span></span>
      <p class="desc desc--compact">We start with rich Caravelle chocolate, known for its velvety smoothness and intense flavor. Then, we add a drizzle of salted caramel, adding a perfect balance of sweetness and a hint of savory richness. Finally, we combine this delightful blend with perfectly steamed milk to create a creamy and indulgent latte that will satisfy even the most discerning palate.</p>
    </article>

    <article class="item item--left" style="top:1434px;right:122px">
      <span class="label label--red">Napoleon Latte<span class="price">$6</span></span>
      <p class="desc desc--compact">We start with our rich espresso, renowned for its bold and robust character. Then, we add a luscious combination of hazelnut and vanilla syrup, creating a symphony of sweetness and nutty richness. As the final touch, we crown this masterpiece with the velvety smoothness of perfectly steamed milk.</p>
    </article>

    <article class="item item--left" style="top:1625px;right:160px">
      <span class="label label--red">Chai Latte<span class="price">$6</span></span>
      <p class="desc desc--compact">Our robust chai tea concentrate, infused with a symphony of cinnamon, cardamom, cloves, and ginger, sets the stage for a journey of aromatic delight. Paired with velvety steamed milk, each sip offers a harmonious blend of bold spices and creamy richness. Topped with a sprinkle of cinnamon, it's the perfect finishing touch to this comforting treat.</p>
    </article>
  </section>

</main>
</body>
</html>
```